Web Design for One for One Organic Soap Company

We need a website design for the company Tidewell Botanics based on the package design per attached.

The design should communicate high end, luxury organic. The site will provide facts about how the spread of disease causes deaths and can be prevented with hand washing. The site will also have a page about why we are passionate about organics and how that relates to our skin including skin facts.
Also, the site should have an e-commerce product page and shopping cart.

Target Market(s)

Educated, health conscious and socially conscious consumers who shop luxury. Target vendors include Larkmont Grocers and Velbrook..

Industry/Entity Type

E-Commerce

Font styles to use
Other font styles liked:
• See attached

Requirements
Must have
• Use of Ying Yang leaf Logo provided.
Based on design provided.

```html
<!DOCTYPE html>
<html lang="en">
<head>
<meta charset="utf-8">
<title>Tidewell Botanics – Organic Soap</title>
<link href="https://fonts.googleapis.com/css2?family=Raleway:wght@300;400;500;600&family=Lato:wght@400;700&display=swap" rel="stylesheet">
<style>
:root{
  --canvas:#e9e7df;
  --page:#ffffff;
  --ink:#3a3a3a;
  --muted:#6b6b6b;
  --brown:#3b2a1f;
  --rust:#a53a22;
  --green:#7dbb2f;
  --panel:#f3f0e9;
  --line:#d9d5cc;
  --link:#a53a22;
  --blue:#3b5b98;
}
*{box-sizing:border-box;margin:0;padding:0}
html,body{width:960px;height:1200px;overflow:hidden}
body{background:var(--canvas);font-family:"Lato",sans-serif;color:var(--ink);position:relative}
.page{position:absolute;left:186px;top:54px;width:588px;height:1110px;background:var(--page)}
.abs{position:absolute}
.toplinks{left:6px;top:10px;width:576px;font-size:8px;display:flex;justify-content:space-between;align-items:center}
.toplinks .right{display:flex;gap:6px;align-items:center}
.currency{width:78px;height:14px;background:#5c5c5c;color:#fff;font-size:8px;padding:2px 6px}
.dash{left:6px;width:576px;border-top:1px dashed #b9b4a8}
.cart{left:438px;top:48px;width:144px;height:24px;border:1px solid var(--line);border-radius:12px;font-size:9px;display:flex;align-items:center}
.cart .count{position:absolute;left:10px;top:-8px;width:16px;height:16px;border-radius:50%;background:var(--green);color:#fff;font-size:7px;text-align:center;line-height:16px}
.cart .total{margin-left:38px}
.cart .checkout{margin-left:auto;height:24px;padding:0 8px;background:var(--green);color:#fff;font-weight:700;border-radius:0 12px 12px 0;line-height:24px;font-size:8px}
.brand{left:6px;top:62px;width:160px;height:50px;display:flex;align-items:center;gap:6px}
.brand .mark{width:26px;height:50px;background:var(--rust);flex:none}
.brand .name{font-family:"Raleway",sans-serif;font-size:14px;font-weight:500;color:var(--brown);line-height:1.3;white-space:nowrap}
.search{left:174px;top:92px;width:209px;height:21px;border:1px solid var(--line);background:#f1f1f1;font-size:8px;padding:5px 10px;color:#555}
.search-btn{left:390px;top:92px;width:63px;height:21px;background:var(--rust);color:#fff;font-size:8px;font-weight:700;text-align:center;line-height:21px}
.assist{right:6px;top:80px;text-align:right;font-size:9px}
.assist b{display:block;font-size:10px;margin-bottom:3px}
.assist .row{display:flex;justify-content:flex-end;align-items:center;gap:6px;margin-top:2px}
.assist .phone{font-size:15px}
.nav{left:0;top:139px;width:588px;display:flex;justify-content:center;gap:8px}
.nav span{border:1px solid #999;font-size:8px;padding:2px 8px;background:#fff}
.nav span.on{background:var(--brown);color:#fff;border-color:var(--brown)}
.hero{left:6px;top:166px;width:576px;height:210px;background:linear-gradient(110deg,#7e2a1e 0%,#b06a50 35%,#d7c2a6 55%,#b57a62 75%,#7a1e14 100%)}
.hero .caption{position:absolute;left:0;bottom:0;width:450px;height:45px;background:rgba(50,38,30,.78);color:#fff;font-family:"Raleway",sans-serif;font-size:15px;padding:5px 8px;line-height:1.2}
.hero .more{position:absolute;right:6px;bottom:6px;width:98px;height:24px;background:var(--rust);border:2px solid #fff;color:#fff;font-size:10px;text-align:center;line-height:20px}
.arrow{top:250px;width:18px;height:40px;background:#fff;font-size:12px;color:#888;line-height:40px;text-align:center}
h2{font-family:"Raleway",sans-serif;font-weight:500;font-size:14px;color:#333}
.socials{right:6px;top:391px;display:flex;gap:3px}
.socials i{display:block;width:22px;height:22px;border-radius:50%;background:#cfcbc3}
.grid{left:6px;top:413px;width:397px;display:grid;grid-template-columns:repeat(3,127px);gap:8px 8px}
.product{border:1px solid var(--line);height:120px;padding:3px}
.product .photo{height:96px}
.product .meta{display:flex;justify-content:space-between;align-items:center;font-size:8px;padding-top:4px}
.product .meta span{display:flex;align-items:center;gap:3px}
.product .like{border:1px solid #b8c4d8;padding:0 3px;font-size:7px;color:var(--blue);background:#eef2f8}
.viewmore{left:260px;top:666px;width:143px;font-size:8px;color:var(--link);text-align:right;border-top:1px dashed #b9b4a8;padding-top:4px}
.side{left:410px;top:413px;width:172px;height:419px;background:var(--panel);padding:6px;font-size:7.5px;line-height:1.32}
.side h3{font-family:"Raleway",sans-serif;font-weight:400;font-size:13px;margin:2px 0 5px}
.side .video{height:78px;background:linear-gradient(#6b6a62,#2f2d29);margin-bottom:6px;position:relative}
.side .video .bar{position:absolute;left:0;bottom:0;width:100%;height:7px;background:#111}
.side .btn{display:inline-block;background:var(--brown);color:#fff;padding:1px 6px;margin:5px 0 6px}
.side .who{text-align:right;font-style:italic;font-weight:700;margin-top:3px}
.side .morelink{color:var(--link);text-align:right;margin-top:6px}
.sale{left:6px;top:710px;width:395px;height:120px;background:linear-gradient(90deg,#e9e0d6,#f3eee6 40%,#d9e2cf 75%,#eef0ea)}
.sale .label{position:absolute;left:0;bottom:12px;background:rgba(60,50,42,.8);color:#fff;font-family:"Raleway",sans-serif;font-size:11px;padding:6px 12px;letter-spacing:.5px}
.sale .buy{position:absolute;right:6px;bottom:8px;width:94px;height:20px;background:var(--rust);color:#fff;font-size:11px;text-align:center;line-height:20px}
.sale .tag{position:absolute;right:8px;top:0;width:22px;height:74px;background:var(--green);color:#fff;font-size:9px;font-weight:700;writing-mode:vertical-rl;transform:rotate(180deg);text-align:center;line-height:22px}
.about{left:6px;top:838px;width:395px;height:145px;border:1px solid var(--line);padding:8px 14px}
.about h4{font-family:"Raleway",sans-serif;font-weight:400;font-size:14px;text-align:center;margin-bottom:10px}
.about p{width:245px;font-size:8px;line-height:1.45}
.about .stones{position:absolute;right:14px;top:38px;width:100px;height:95px;background:linear-gradient(#c2c69a,#8a9458)}
.fanbox{left:410px;top:838px;width:172px;height:192px;border:1px solid var(--line);padding:12px}
.fanbox .in{border:1px solid #c9c9c9;height:100%;font-size:7px}
.fanbox .head{background:var(--blue);color:#fff;font-weight:700;font-size:9px;padding:2px 4px}
.fanbox .page-row{display:flex;gap:4px;padding:4px}
.fanbox .sq{width:26px;height:34px;background:var(--rust)}
.fanbox .btnlike{display:inline-block;background:var(--blue);color:#fff;padding:0 3px;margin-top:3px}
.fanbox .faces{display:grid;grid-template-columns:repeat(4,1fr);gap:3px;padding:4px}
.fanbox .faces i{display:block;height:26px;background:#c6b8a8}
.news{left:6px;top:992px;width:395px;height:38px;background:#e4e1dc;display:flex;align-items:center;padding:0 6px}
.news .field{width:108px;height:20px;background:#fff;border:1px solid #bbb;font-size:8px;padding:4px}
.news .go{height:20px;background:var(--rust);color:#fff;font-size:8px;font-weight:700;padding:0 6px;line-height:20px}
.news .txt{margin-left:12px;font-size:7px;font-weight:700}
.news .txt b{display:block;font-size:11px;font-family:"Raleway",sans-serif}
.footband{left:0;top:1040px;width:588px;height:8px;background:linear-gradient(#f1efea,#fff)}
.ficons{left:6px;top:1067px;display:flex;gap:3px}
.ficons i{display:block;width:14px;height:14px;border-radius:50%;background:#666}
.legal{left:6px;top:1095px;font-size:8px;color:#444}
.pay{top:1085px;height:26px;border:1px solid #ccc;font-size:8px;font-weight:700;text-align:center;line-height:24px}
</style>
</head>
<body>
<div class="page">
  <div class="abs toplinks">
    <span>Why Choose Organics? / Articles / Our Blog</span>
    <span class="right">Contact Us | Home | My Account | Wishlist | Login | Signup | Currency: <span class="currency">USD</span></span>
  </div>
  <div class="abs dash" style="top:26px"></div>

  <div class="abs cart"><span class="count">20</span><span class="total">$200.00</span><span class="checkout">Checkout</span></div>

  <div class="abs brand"><span class="mark"></span><span class="name">Tidewell Botanics<br>organic soap</span></div>
  <div class="abs search">Enter product name or code</div>
  <div class="abs search-btn">SEARCH</div>

  <div class="abs assist">
    <b>Need Assistance?</b>
    <div class="row">
      <svg width="12" height="9" viewBox="0 0 12 9"><rect x=".5" y=".5" width="11" height="8" fill="none" stroke="#555"/><path d="M.5 .5 6 5 11.5 .5" fill="none" stroke="#555"/></svg>
      sales@tidewellbotanics.com</div>
    <div class="row phone">
      <svg width="12" height="12" viewBox="0 0 12 12"><path d="M2 1 4 1 5 4 3.5 5C4.5 7 5 7.5 7 8.5L8 7 11 8V10C11 11 10 11 9 11 5 10.5 1.5 7 1 3 1 2 1 1 2 1Z" fill="#555"/></svg>
      0123 555 0187</div>
  </div>

  <div class="abs dash" style="top:126px"></div>

  <nav class="abs nav">
    <span class="on">Products</span><span>Natural Soaps</span><span>Gifts</span><span>Top sellers</span><span>For women</span><span>For men</span><span>Gift sets</span><span>Facial care starter sets</span>
  </nav>

  <div class="abs hero" role="img" aria-label="Photo: hands holding an oval bar of natural soap">
    <div class="caption">We are passionate about<br>organics and how that relates to our skin including skin facts.</div>
    <div class="more">Learn More</div>
  </div>
  <div class="abs arrow" style="left:0;border-radius:0 20px 20px 0">‹</div>
  <div class="abs arrow" style="right:0;border-radius:20px 0 0 20px">›</div>

  <h2 class="abs" style="left:6px;top:390px">Top Selling Products</h2>
  <div class="abs socials"><i></i><i></i><i></i><i></i></div>

  <div class="abs grid">
    <div class="product"><div class="photo" role="img" aria-label="Stacked yellow and white soap bars tied with twine" style="background:linear-gradient(#f0e6a0,#e8d45a)"></div><div class="meta"><span>$40.00 <svg width="10" height="8" viewBox="0 0 10 8"><path d="M0 1H2L3 6H8.5L9.5 2H2.5" fill="none" stroke="#666"/></svg></span><span class="like">Like</span></div></div>
    <div class="product"><div class="photo" role="img" aria-label="Orange soap with sliced orange" style="background:linear-gradient(#f2c078,#e27a25)"></div><div class="meta"><span>$40.00 <svg width="10" height="8" viewBox="0 0 10 8"><path d="M0 1H2L3 6H8.5L9.5 2H2.5" fill="none" stroke="#666"/></svg></span><span class="like">Like</span></div></div>
    <div class="product"><div class="photo" role="img" aria-label="Lavender and green soap bars" style="background:linear-gradient(#c9bde0,#9fb08a)"></div><div class="meta"><span>$40.00 <svg width="10" height="8" viewBox="0 0 10 8"><path d="M0 1H2L3 6H8.5L9.5 2H2.5" fill="none" stroke="#666"/></svg></span><span class="like">Like</span></div></div>
    <div class="product"><div class="photo" role="img" aria-label="White soap bar with a green leaf" style="background:linear-gradient(#e6e4d4,#b8b49a)"></div><div class="meta"><span>$40.00 <svg width="10" height="8" viewBox="0 0 10 8"><path d="M0 1H2L3 6H8.5L9.5 2H2.5" fill="none" stroke="#666"/></svg></span><span class="like">Like</span></div></div>
    <div class="product"><div class="photo" role="img" aria-label="Round oatmeal soaps" style="background:linear-gradient(#f1e9dc,#d9c8ad)"></div><div class="meta"><span>$40.00 <svg width="10" height="8" viewBox="0 0 10 8"><path d="M0 1H2L3 6H8.5L9.5 2H2.5" fill="none" stroke="#666"/></svg></span><span class="like">Like</span></div></div>
    <div class="product"><div class="photo" role="img" aria-label="Gift stack of colourful soaps with ribbon" style="background:linear-gradient(#f3d58b,#8fb46a)"></div><div class="meta"><span>$40.00 <svg width="10" height="8" viewBox="0 0 10 8"><path d="M0 1H2L3 6H8.5L9.5 2H2.5" fill="none" stroke="#666"/></svg></span><span class="like">Like</span></div></div>
  </div>
  <div class="abs viewmore">View more products →</div>

  <aside class="abs side">
    <h3>Why Use Organic Soap?</h3>
    <div class="video" role="img" aria-label="Video about washing hands with organic soap"><div class="bar"></div></div>
    <h3>Why Shop With Us?</h3>
    <p>The design should communicate high end, luxury organic. The site will provide facts about how the spread of disease causes deaths and can be prevented with hand washing. The site will also have a page about why we are passionate about organics and how that relates to our skin including skin facts. SAMPLE TEXT</p>
    <span class="btn">learn more</span>
    <h3>Testimonials</h3>
    <p>"The design should communicate high end, luxury organic. The site will provide facts about how the spread of disease causes deaths and can be prevented with hand washing. The site will also have a page about why we are passionate about organics and how that relates to our skin including skin facts. SAMPLE TEXT"</p>
    <p class="who">Marion, Homemaker<br>USA</p>
    <p class="morelink">More testimonials →</p>
  </aside>

  <h2 class="abs" style="left:6px;top:690px">On Sale Now</h2>
  <div class="abs sale" role="img" aria-label="Bath scene with pink, yellow and red soap bars on a leaf">
    <div class="label">Soap name here</div>
    <div class="buy">Buy Now</div>
    <div class="tag">10% OFF</div>
  </div>

  <section class="abs about">
    <h4>100% Original... natural, handmade, organic</h4>
    <p>Our pure and mild natural soaps are handmade in the old world tradition with certified organic vegetable oils, wild and organic herbs, and only pure essential oils. Neque porro quisquam est qui dolorem ipsum quia dolor sit amet, consectetur, adipisci velit.<br>Neque porro quisquam est qui dolorem ipsum quia dolor sit amet, consectetur, adipisci velitNeque porro quisquam est qui dolorem ipsum quia dolor sit amet, consectetur, adipisci velit</p>
    <div class="stones" role="img" aria-label="Photo: stack of round green soaps"></div>
  </section>

  <div class="abs fanbox">
    <div class="in">
      <div class="head">Fan Page</div>
      <div class="page-row"><span class="sq"></span><div>Tidewell Botanics<br>Organic Soaps<br><span class="btnlike">Like</span></div></div>
      <div style="padding:2px 4px;border-top:1px solid #ddd">2,747 people like <span style="color:var(--blue)">Tidewell Botanics Soaps</span></div>
      <div class="faces" role="img" aria-label="Grid of follower avatars"><i></i><i></i><i></i><i></i><i></i><i></i><i></i><i></i></div>
    </div>
  </div>

  <div class="abs news">
    <span class="field">reader@mailbox.net</span><span class="go">Get Newsletter</span>
    <span class="txt"><b>Stay informed!</b>We add new products frequently. SignUp for FREE newsletter</span>
  </div>

  <div class="abs footband"></div>
  <div class="abs ficons"><i></i><i></i><i></i><i></i><i></i><i></i></div>
  <div class="abs legal">Click here for legal | Media | Legal | Site Map &nbsp;/&nbsp; All rights are reserved © 2014 tidewellbotanics.com</div>
  <div class="abs pay" style="left:382px;width:70px;color:#2a4a8a;background:#f6f3e6">Pay Online</div>
  <div class="abs pay" style="left:458px;width:124px;color:#444">Quick Checkout</div>
</div>
</body>
</html>
```